Design Challege - Simplify a Complex Message

We have a new website design, but one of the pages presents a particular problem.

Our company does ERP implementations. We have developed a proprietary approach to these implementations based on the idea that you must get eight (and only eight) things right. These eight things are listed below, summarized in one or two words each:

1. Value
2. Capability
3. Functionality
4. Data
5. Technology
6. Change Leadership
7. Quality
8. Governance

Each of these eight things can be summarized in a short paragraph, but when you combine all eight summaries with a brief introductory text, the result is a lot of text - so much text that the casual surfer may be overwhelmed by it.

The winning design will find an engaging way to present the information in a way that presents a high-level summary, using icons and one- or two-word descriptions above but revealing more information when clicked.

Our current design for this information, with a paragraph describing the eight elements in a table, is included as an upload in PDF and Microsoft Word formats. We are looking for a creative way to display these eight things, showing the detail only when the user wants to see it.

The website is being built in WordPress, using Elementor as a page builder.

We will implement (code) the page, but the winner will be asked to specify the widget or other add-in if one is required.

The design does not need to include a header or footer, we have those.

Target Market(s)

Business executives working in technology

Industry/Entity Type

Any

Number of Pages Required

1 page

Font styles to use
Sans Serif

Requirements
Must have
• A design for the body of the page, but not the header or footer.
Nice to have
• Unique icons or images appropriate for each of the eight things.
Should not have
• A lot of text on one page

```html
<!DOCTYPE html>
<html lang="en">
<head>
<meta charset="utf-8">
<title>ERP Implementations – Eight Things to Get Right</title>
<link href="https://fonts.googleapis.com/css2?family=Inter+Tight:wght@400;500;600;700&display=swap" rel="stylesheet">
<style>
  :root{
    --bg:#f9d6d7;
    --card:#ffffff;
    --ink:#111111;
    --muted:#3d3d3d;
    --line:#e6e6e6;
    --tile-border:#ececec;
    --icon-bg:#f1f1f1;
    --icon-ink:#3a3a3a;
    --dim:#4d4d4d;
    --dim-tile-border:#565656;
    --dim-icon-bg:#474747;
    --dim-ink:#1c1c1c;
    --dim-muted:#262626;
    --accent:#1a7cf0;
  }
  *{box-sizing:border-box;margin:0;padding:0}
  html,body{width:1200px;height:467px;overflow:hidden}
  body{background:var(--bg);font-family:"Inter Tight",sans-serif;color:var(--ink);position:relative}

  .panel{position:absolute;top:83px;width:515px;height:300px;border-radius:4px;padding:0 12px;overflow:hidden}
  .panel--light{left:57px;background:var(--card)}
  .panel--dim{left:628px;background:var(--dim)}

  .panel__title{font-size:9.5px;font-weight:700;margin-top:13px;line-height:12px}
  .panel__rule{height:1px;background:var(--line);margin-top:8px}
  .panel__sub{font-size:8px;font-weight:600;color:var(--muted);margin-top:7px;line-height:12px}
  .panel__intro{font-size:7.9px;color:var(--muted);line-height:12.1px;letter-spacing:-0.02px}

  .grid{position:absolute;left:12px;top:99px;display:grid;grid-template-columns:241px 241px;column-gap:11px;row-gap:10px}
  .tile{height:40px;border:1px solid var(--tile-border);border-radius:4px;display:flex;align-items:center;padding-left:6px;padding-right:24px;position:relative}
  .tile__icon{width:28px;height:28px;border-radius:4px;background:var(--icon-bg);display:flex;align-items:center;justify-content:center;flex:none}
  .tile__icon svg{width:17px;height:17px;stroke:var(--icon-ink);fill:none;stroke-width:1.6;stroke-linecap:round;stroke-linejoin:round}
  .tile__text{margin-left:8px;white-space:nowrap;min-width:0}
  .tile__name{font-size:10px;font-weight:600;line-height:12px}
  .tile__desc{font-size:7.7px;color:var(--muted);line-height:11px;margin-top:1px}
  .tile__chev{position:absolute;right:10px;top:14px;width:8px;height:11px;stroke:var(--ink);fill:none;stroke-width:1.5}

  .panel--dim .panel__title,.panel--dim .tile__name{color:var(--dim-ink)}
  .panel--dim .panel__sub,.panel--dim .panel__intro,.panel--dim .tile__desc{color:var(--dim-muted)}
  .panel--dim .panel__rule{background:#5a5a5a}
  .panel--dim .tile{border-color:var(--dim-tile-border)}
  .panel--dim .tile__icon{background:var(--dim-icon-bg)}
  .panel--dim .tile__icon svg{stroke:#1f1f1f}
  .panel--dim .tile__chev{stroke:#1a1a1a}

  .close{position:absolute;left:641px;top:95px;width:13px;height:13px}

  .modal{position:absolute;left:742px;top:150px;width:288px;height:166px;background:var(--card);border-radius:4px;padding:8px 6px 0 7px;display:flex}
  .modal__icon{width:28px;height:28px;border-radius:4px;background:var(--icon-bg);display:flex;align-items:center;justify-content:center;flex:none}
  .modal__icon svg{width:17px;height:17px;stroke:var(--icon-ink);fill:none;stroke-width:1.6;stroke-linecap:round;stroke-linejoin:round}
  .modal__body{margin-left:8px;width:239px}
  .modal__title{font-size:10px;font-weight:600;line-height:12px;margin-top:-1px}
  .modal__text{font-size:7.7px;color:var(--muted);line-height:13.6px;margin-top:2px}

  .connector{position:absolute;left:0;top:0;width:1200px;height:467px;pointer-events:none}
</style>
</head>
<body>

<svg width="0" height="0" style="position:absolute">
  <defs>
    <symbol id="i-diamond" viewBox="0 0 24 24"><path d="M5 10l3-3h8l3 3-7 9z"/><path d="M5 10h14M12 19l-3-9 3-3 3 3z"/><path d="M12 2v2M6 3l1 2M18 3l-1 2"/></symbol>
    <symbol id="i-chip" viewBox="0 0 24 24"><circle cx="11" cy="12" r="6"/><path d="M11 6v12M11 9h6M11 12h8M11 15h6M3 12h2"/></symbol>
    <symbol id="i-team" viewBox="0 0 24 24"><circle cx="12" cy="10" r="2.5"/><path d="M8 18c0-3 2-4.5 4-4.5s4 1.5 4 4.5"/><circle cx="4" cy="6" r="1.5"/><circle cx="20" cy="6" r="1.5"/><circle cx="4" cy="18" r="1.5"/><circle cx="20" cy="18" r="1.5"/><path d="M5 7l5 2M19 7l-5 2"/></symbol>
    <symbol id="i-lead" viewBox="0 0 24 24"><circle cx="7" cy="6" r="2"/><path d="M7 9l-1 6-2 5M7 12l3 2M6 15l3 5"/><circle cx="16" cy="5" r="2"/><path d="M16 8v6M13 11h6M14 20l2-6 2 6"/></symbol>
    <symbol id="i-gears" viewBox="0 0 24 24"><circle cx="8" cy="8" r="3.5"/><circle cx="8" cy="8" r="1"/><circle cx="16" cy="16" r="3.5"/><circle cx="16" cy="16" r="1"/><path d="M8 2.5v2M8 11.5v2M2.5 8h2M11.5 8h2M16 10.5v2M16 19.5v2M10.5 16h2M19.5 16h2"/></symbol>
    <symbol id="i-quality" viewBox="0 0 24 24"><circle cx="12" cy="10" r="6"/><path d="M12 7l1 2 2 .3-1.5 1.4.4 2.1-1.9-1-1.9 1 .4-2.1L9 9.3l2-.3z"/><path d="M8 15l-2 6 3-1 2 2 1-5M16 15l2 6-3-1-2 2-1-5"/></symbol>
    <symbol id="i-data" viewBox="0 0 24 24"><path d="M3 8h6l2 2h10v9H3z"/><path d="M6 8V5h5l2 2h6v3"/><path d="M6 15h2M10 15h2"/></symbol>
    <symbol id="i-gov" viewBox="0 0 24 24"><circle cx="12" cy="8" r="4"/><path d="M12 2v2M6 5l1.5 1.5M18 5l-1.5 1.5M4 10h2M18 10h2"/><path d="M4 21v-4a2 2 0 014 0v4M10 21v-4a2 2 0 014 0v4M16 21v-4a2 2 0 014 0v4"/></symbol>
    <symbol id="chev" viewBox="0 0 8 11"><path d="M2 1l4.5 4.5L2 10"/></symbol>
  </defs>
</svg>

<section class="panel panel--light" aria-label="ERP Implementations overview">
  <h2 class="panel__title">ERP Implementations</h2>
  <div class="panel__rule"></div>
  <h3 class="panel__sub">Eight Things to Get Right</h3>
  <p class="panel__intro">Like the roots and branches of a tree, there are many considerations in an ERP implementation. Focus too much on the minor details, and you can lose sight of the tree. In an ERP implementation, you must get eight major things right to be successful. Ignore any of them, and your implementation will fail. Get them right, and you will likely succeed.</p>
  <div class="grid">
    <div class="tile"><div class="tile__icon"><svg><use href="#i-diamond"/></svg></div><div class="tile__text"><div class="tile__name">Value</div><div class="tile__desc">The project must provide value that significantly</div></div><svg class="tile__chev"><use href="#chev"/></svg></div>
    <div class="tile"><div class="tile__icon"><svg><use href="#i-chip"/></svg></div><div class="tile__text"><div class="tile__name">Technology</div><div class="tile__desc">What is the platform for the system?</div></div><svg class="tile__chev"><use href="#chev"/></svg></div>
    <div class="tile"><div class="tile__icon"><svg><use href="#i-team"/></svg></div><div class="tile__text"><div class="tile__name">Capability</div><div class="tile__desc">The company and the implementation team</div></div><svg class="tile__chev"><use href="#chev"/></svg></div>
    <div class="tile"><div class="tile__icon"><svg><use href="#i-lead"/></svg></div><div class="tile__text"><div class="tile__name">Change Leadership</div><div class="tile__desc">Change leadership often called change</div></div><svg class="tile__chev"><use href="#chev"/></svg></div>
    <div class="tile"><div class="tile__icon"><svg><use href="#i-gears"/></svg></div><div class="tile__text"><div class="tile__name">Functionality</div><div class="tile__desc">An ERP project must support required business</div></div><svg class="tile__chev"><use href="#chev"/></svg></div>
    <div class="tile"><div class="tile__icon"><svg><use href="#i-quality"/></svg></div><div class="tile__text"><div class="tile__name">Quality</div><div class="tile__desc">Quality is multi-dimensional</div></div><svg class="tile__chev"><use href="#chev"/></svg></div>
    <div class="tile"><div class="tile__icon"><svg><use href="#i-data"/></svg></div><div class="tile__text"><div class="tile__name">Data</div><div class="tile__desc">ERP systems are data-hungry creatures.</div></div><svg class="tile__chev"><use href="#chev"/></svg></div>
    <div class="tile"><div class="tile__icon"><svg><use href="#i-gov"/></svg></div><div class="tile__text"><div class="tile__name">Governance</div><div class="tile__desc">ERP projects require both management</div></div><svg class="tile__chev"><use href="#chev"/></svg></div>
  </div>
</section>

<section class="panel panel--dim" aria-label="ERP Implementations with Technology detail open">
  <h2 class="panel__title">ERP Implementations</h2>
  <div class="panel__rule"></div>
  <h3 class="panel__sub">Eight Things to Get Right</h3>
  <p class="panel__intro">Like the roots and branches of a tree, there are many considerations in an ERP implementation. Focus too much on the minor details, and you can lose sight of the tree. In an ERP implementation, you must get eight major things right to be successful. Ignore any of them, and your implementation will fail. Get them right, and you will likely succeed.</p>
  <div class="grid">
    <div class="tile"><div class="tile__icon"><svg><use href="#i-diamond"/></svg></div><div class="tile__text"><div class="tile__name">Value</div><div class="tile__desc">The project must provide value that significantly</div></div><svg class="tile__chev"><use href="#chev"/></svg></div>
    <div class="tile"><div class="tile__icon"><svg><use href="#i-chip"/></svg></div><div class="tile__text"><div class="tile__name">Technology</div><div class="tile__desc">What is the platform for the system?</div></div><svg class="tile__chev"><use href="#chev"/></svg></div>
    <div class="tile"><div class="tile__icon"><svg><use href="#i-team"/></svg></div><div class="tile__text"><div class="tile__name">Capability</div><div class="tile__desc">The company and the implementation team</div></div><svg class="tile__chev"><use href="#chev"/></svg></div>
    <div class="tile"><div class="tile__icon"><svg><use href="#i-lead"/></svg></div><div class="tile__text"><div class="tile__name">Change Leadership</div><div class="tile__desc">Change leadership often called change</div></div><svg class="tile__chev"><use href="#chev"/></svg></div>
    <div class="tile"><div class="tile__icon"><svg><use href="#i-gears"/></svg></div><div class="tile__text"><div class="tile__name">Functionality</div><div class="tile__desc">An ERP project must support required business</div></div><svg class="tile__chev"><use href="#chev"/></svg></div>
    <div class="tile"><div class="tile__icon"><svg><use href="#i-quality"/></svg></div><div class="tile__text"><div class="tile__name">Quality</div><div class="tile__desc">Quality is multi-dimensional</div></div><svg class="tile__chev"><use href="#chev"/></svg></div>
    <div class="tile"><div class="tile__icon"><svg><use href="#i-data"/></svg></div><div class="tile__text"><div class="tile__name">Data</div><div class="tile__desc">ERP systems are data-hungry creatures.</div></div><svg class="tile__chev"><use href="#chev"/></svg></div>
    <div class="tile"><div class="tile__icon"><svg><use href="#i-gov"/></svg></div><div class="tile__text"><div class="tile__name">Governance</div><div class="tile__desc">ERP projects require both management</div></div><svg class="tile__chev"><use href="#chev"/></svg></div>
  </div>
</section>

<svg class="close" viewBox="0 0 13 13" aria-label="Close">
  <circle cx="6.5" cy="6.5" r="5.6" fill="#1c1c1c" stroke="#ffffff" stroke-width="1.2"/>
  <path d="M4.4 4.4l4.2 4.2M8.6 4.4l-4.2 4.2" stroke="#ffffff" stroke-width="1.2" stroke-linecap="round"/>
</svg>

<div class="modal" role="dialog" aria-label="Technology">
  <div class="modal__icon"><svg><use href="#i-diamond"/></svg></div>
  <div class="modal__body">
    <h4 class="modal__title">Technology</h4>
    <p class="modal__text">What is the platform for the system? Is it offered by a vendor that will be around for as long as your system? Will it integrate with your other systems? Are resources available to support it? Can you change it without painting yourself into a corner? Will your technology scale as you grow?What is the platform for the system? Is it offered by a vendor that will be around for as long as your system? Will it integrate with your other systems? Are resources available to support it? Can you change it without painting yourself into a corner? Will your technology scale as you grow?</p>
  </div>
</div>

<svg class="connector" viewBox="0 0 1200 467">
  <circle cx="563" cy="201" r="3" fill="var(--accent)"/>
  <path d="M563 201 C 585 207, 600 208, 598 200 C 595 185, 592 150, 612 164 M612 164 C 618 162, 622 165, 626 167" stroke="var(--accent)" stroke-width="1.2" fill="none"/>
  <path d="M620 161 L627 167 L619 170" stroke="var(--accent)" stroke-width="1.2" fill="none" stroke-linecap="round" stroke-linejoin="round"/>
</svg>

</body>
</html>
```